R&T Photography (business cards)

Business cards for a photography business. We also photographs events, portraits, headshots.
Colors: Vanilla w/ dark blue (not Aqua or Navy)
Website: randtphotography482-mailbox.net
Email: randtphotography76@mailbox.net
Company Name: R&T Photography
Letter style/font for company name is French Script
We would like a card that somehow delivers a combination of softness, confidence and strength.

Target Market(s)

Wedding clients

Industry/Entity Type

Business

Font styles to use
Decorative
Script

Colors
0d5ba7
3176b5
5c5c5c
dbdbdb

Requirements
Must have
• Bold and/or raised print for company name. Website should also stand out. Telephone contact numbers are:
• (555) 214-7730
• (555) 862-3046
• Website: RandTPhotohraphy482-mailbox.net
• Business address: PO Box 6204, Orlando, FL 32899
• Back of card should state: referrals are welcome.
Nice to have
• some lace/scroll
Should not have
• Non-metallic.

```html
<!DOCTYPE html>
<html lang="en">
<head>
<meta charset="utf-8">
<title>R&amp;T Photography — Business Cards</title>
<link rel="stylesheet" href="https://fonts.googleapis.com/css2?family=Parisienne&family=Cormorant+Garamond:ital,wght@1,500;1,700&family=Kaushan+Script&family=Montserrat:wght@400&display=swap">
<style>
  :root {
    --backdrop: #e9e4dc;
    --card-blue: #1560ad;
    --card-blue-light: #3176b5;
    --card-grey: #d6d7d9;
    --lace-grey: #e4e5e6;
    --ink-white: #ffffff;
    --ink-dark: #111111;
    --ink-link: #2b2f8f;
    --rule-white: rgba(255,255,255,0.85);
  }
  * { margin: 0; padding: 0; box-sizing: border-box; }
  html, body {
    width: 1000px; height: 1200px; overflow: hidden;
    background: var(--backdrop);
  }
  .sheet { position: relative; width: 1000px; height: 1200px; }
  .card {
    position: absolute; left: 57px; width: 887px; height: 520px;
    box-shadow: 0 4px 10px rgba(0,0,0,0.35);
    overflow: hidden;
  }
  /* Front */
  .card--front { top: 53px; background: var(--card-blue); color: var(--ink-white); }
  .front__edge-rule {
    position: absolute; left: 31px; top: 0; bottom: 0; width: 2px;
    background: var(--rule-white);
  }
  .front__scroll {
    position: absolute; left: 17px; top: 180px; width: 30px; height: 145px;
    background: var(--card-blue-light); border-radius: 15px;
    border: 2px solid rgba(255,255,255,0.7);
  }
  .front__lace {
    position: absolute; right: 0; top: 0; width: 410px; height: 220px;
    background: radial-gradient(ellipse at top right, rgba(255,255,255,0.7) 0%, rgba(255,255,255,0.35) 45%, rgba(255,255,255,0) 72%);
  }
  .front__tagline {
    position: absolute; left: 65px; top: 18px;
    font-family: "Montserrat", sans-serif; font-size: 15px;
  }
  .front__name {
    position: absolute; left: 0; right: 0; top: 185px; text-align: center;
    font-family: "Parisienne", cursive; font-size: 84px; line-height: 1;
    text-shadow: 1px 2px 3px rgba(0,0,0,0.45);
  }
  .front__website {
    position: absolute; left: 0; right: 0; top: 380px; text-align: center;
    font-family: "Cormorant Garamond", serif; font-style: italic; font-weight: 700;
    font-size: 26px;
  }
  .front__divider {
    position: absolute; left: 53px; right: 58px; top: 424px; height: 2px;
    background: var(--rule-white);
  }
  .front__contacts, .front__address {
    position: absolute; left: 0; right: 0; text-align: center;
    font-family: "Cormorant Garamond", serif; font-style: italic; font-weight: 500;
    font-size: 25px;
  }
  .front__contacts { top: 434px; }
  .front__address { top: 468px; }
  /* Back */
  .card--back { top: 617px; background: var(--card-grey); }
  .back__lace {
    position: absolute; left: 300px; top: 0; right: 0; bottom: 0;
    background: linear-gradient(120deg, var(--lace-grey), var(--card-grey) 60%, var(--lace-grey));
  }
  .back__photo-frame {
    position: absolute; left: 50px; top: 60px; width: 263px; height: 402px;
    background: #e9e9ea; padding: 5px;
  }
  .back__photo {
    width: 100%; height: 100%;
    background: linear-gradient(180deg, #8a8078 0%, #d9d6cf 35%, #f1f0ec 65%, #c9a860 100%);
  }
  .back__referral {
    position: absolute; left: 385px; top: 230px;
    font-family: "Kaushan Script", cursive; font-size: 44px; color: var(--ink-dark);
  }
  .back__website {
    position: absolute; left: 436px; top: 289px;
    font-family: "Cormorant Garamond", serif; font-style: italic; font-weight: 700;
    font-size: 19px; color: var(--ink-link);
  }
</style>
</head>
<body>
<main class="sheet">
  <section class="card card--front">
    <div class="front__lace" role="img" aria-label="White lace ornament in the top right corner"></div>
    <div class="front__edge-rule"></div>
    <div class="front__scroll" role="img" aria-label="White scroll ornament on the left rule"></div>
    <p class="front__tagline">Moments of Happiness. A Lifetime of Memories!</p>
    <h1 class="front__name">R&amp;T Photography</h1>
    <p class="front__website">www.randtphotography482-mailbox.net</p>
    <div class="front__divider"></div>
    <p class="front__contacts">(555) 214-7730 | (555) 862-3046 | randtphotography76@mailbox.net</p>
    <p class="front__address">PO Box 6204, Orlando, FL 32899</p>
  </section>

  <section class="card card--back">
    <div class="back__lace" role="img" aria-label="Faint white floral lace pattern"></div>
    <div class="back__photo-frame">
      <div class="back__photo" role="img" aria-label="Photo of a wedding champagne flute with heart charm on a white table"></div>
    </div>
    <p class="back__referral">referrals are welcome</p>
    <p class="back__website">www.randtphotography482-mailbox.net</p>
  </section>
</main>
</body>
</html>
```